Business Card Revision

Need to redesign my business cards for a new professional look. We are a courier company. You can go to www.qvroutefast.com to see what we do. The trucks have an old company name (Nimble) on them but that is the company we are just now
changing the name.

Target Market(s)

Potential clients. We service the automotive, plumbing, printing, air freight industries as well as many others.

Industry/Entity Type

Business

Contact Information for Business Card

QVrushline
20583 Palmer Fenwick Parkway
Cincinnati, Oh 45317

Howard T. Lassiter
President

howie@qvroutefast.com

Main: (513) 555-0147

```html
<!DOCTYPE html>
<html lang="en">
<head>
<meta charset="utf-8">
<title>QVrushline Business Card</title>
<link rel="stylesheet" href="https://fonts.googleapis.com/css2?family=Source+Sans+3:wght@400;600;700&display=swap">
<style>
  :root {
    --brand-green: #3bb54a;
    --brand-blue: #1176c1;
    --card-white: #ffffff;
    --stage: #ecebe8;
  }
  * { margin: 0; padding: 0; box-sizing: border-box; }
  html, body { width: 1200px; height: 900px; overflow: hidden; }
  body {
    position: relative;
    background: var(--stage);
    font-family: "Source Sans 3", "Myriad Pro", sans-serif;
  }
  .card {
    position: absolute;
    width: 556px;
    height: 342px;
    overflow: hidden;
    box-shadow: 0 6px 18px rgba(0,0,0,0.12);
  }
  .card-front { left: 238px; top: 62px; background: var(--card-white); }
  .card-back  { left: 458px; top: 518px; background: var(--brand-blue); }
  .front-graphic { position: absolute; inset: 0; }
  .contact-block {
    position: absolute;
    left: 35px;
    top: 86px;
    color: var(--card-white);
  }
  .holder-name { font-size: 18px; font-weight: 600; line-height: 1.1; }
  .holder-title { font-size: 15px; font-weight: 400; margin-top: 2px; }
  .address { font-size: 15px; line-height: 20px; margin-top: 20px; }
  .contact-list { list-style: none; margin-top: 18px; font-size: 15px; line-height: 20px; }
  .contact-list li { display: flex; align-items: center; gap: 8px; }
  .contact-list svg { width: 12px; height: 12px; fill: var(--card-white); flex: none; }
  .company-name {
    position: absolute;
    inset: 0;
    display: flex;
    align-items: center;
    justify-content: center;
    color: var(--card-white);
    font-size: 64px;
    font-weight: 700;
    letter-spacing: 1px;
  }
</style>
</head>
<body>
  <section class="card card-front">
    <svg class="front-graphic" viewBox="0 0 556 342" aria-hidden="true">
      <polygon points="0,0 496,0 173,342 0,342" fill="var(--brand-green)"/>
      <polygon points="556,66 556,342 287,342" fill="var(--brand-blue)"/>
    </svg>
    <div class="contact-block">
      <div class="holder-name">Howard T. Lassiter</div>
      <div class="holder-title">President</div>
      <div class="address">20583 Palmer Fenwick Parkway<br>Cincinnati, Oh 45317</div>
      <ul class="contact-list">
        <li><svg viewBox="0 0 24 24"><path d="M6.6 10.8a15.1 15.1 0 0 0 6.6 6.6l2.2-2.2a1 1 0 0 1 1-.25 11.4 11.4 0 0 0 3.6.57 1 1 0 0 1 1 1V20a1 1 0 0 1-1 1A17 17 0 0 1 3 4a1 1 0 0 1 1-1h3.5a1 1 0 0 1 1 1c0 1.25.2 2.45.57 3.57a1 1 0 0 1-.25 1z"/></svg>(513) 555-0147</li>
        <li><svg viewBox="0 0 24 24"><path d="M2 5h20v14H2z M3 6l9 7 9-7" stroke="var(--brand-green)" stroke-width="1.5"/></svg>howie@qvroutefast.com</li>
        <li><svg viewBox="0 0 24 24"><circle cx="12" cy="12" r="10"/><path d="M2 12h20M12 2c3 3 3 17 0 20M12 2c-3 3-3 17 0 20" stroke="var(--brand-green)" stroke-width="1.6" fill="none"/></svg>www.qvroutefast.com</li>
      </ul>
    </div>
  </section>

  <section class="card card-back">
    <div class="company-name">QVrushline</div>
  </section>
</body>
</html>
```